Quillfen Holdings Business Card Design Project

We have recently rebranded and would like to design new business cards that incorporate the corporate logo - double sided cards with corporate logo on one side and contact details on the other

Target Market(s)

Sophisticated and high net worth investors and finance industry professionals

Industry/Entity Type

Funds Management

Contact Information for Business Card

The card should prominently feature the company name and logo. Other details will be standard contact details for each staff member - name, address, phone, email, website

Colors
0054AA
0677BA
7BADD7
CADEEF
E8F1F8

Requirements
Must have
• Double-sided design with one side prominently featuring the corporate logo and the other side with all standard contact details

```html
<!DOCTYPE html>
<html lang="en">
<head>
<meta charset="utf-8">
<title>Quillfen Holdings – Business Card</title>
<link rel="stylesheet" href="https://fonts.googleapis.com/css2?family=Cinzel:wght@500&family=Arimo:wght@400&display=swap">
<style>
  :root {
    --navy: #1f4576;
    --navy-deep: #1a3b66;
    --paper: #ffffff;
    --ink: #1b1b1b;
    --backdrop: #c4c4c4;
    --rule: rgba(255,255,255,0.45);
  }
  * { box-sizing: border-box; margin: 0; padding: 0; }
  html, body { width: 1200px; height: 800px; overflow: hidden; }
  body {
    background: var(--backdrop);
    display: flex;
    align-items: center;
    justify-content: center;
    gap: 40px;
  }
  .card {
    width: 540px;
    height: 310px;
    position: relative;
    overflow: hidden;
    box-shadow: 0 10px 24px rgba(0,0,0,0.25);
  }
  /* Front: contact side */
  .card--front { background: var(--paper); }
  .brand {
    position: absolute;
    top: 0; left: 0; right: 0;
    height: 112px;
    display: flex;
    align-items: center;
    justify-content: center;
    font-family: 'Cinzel', serif;
    font-weight: 500;
    font-size: 38px;
    color: var(--navy);
    letter-spacing: 1px;
  }
  .band {
    position: absolute;
    top: 112px; left: 0; right: 0;
    height: 108px;
    background: var(--navy);
    display: flex;
    align-items: center;
    justify-content: center;
    gap: 22px;
    color: var(--paper);
  }
  .person { text-align: right; }
  .person__name {
    font-family: 'Cinzel', serif;
    font-weight: 500;
    font-size: 22px;
    letter-spacing: 0.5px;
  }
  .person__title {
    font-family: 'Arimo', sans-serif;
    font-size: 15px;
    margin-top: 2px;
  }
  .band__divider {
    width: 1px;
    height: 64px;
    background: var(--rule);
  }
  .contact {
    font-family: 'Arimo', sans-serif;
    font-size: 15px;
    line-height: 1.4;
    list-style: none;
  }
  .address {
    position: absolute;
    top: 220px; left: 0; right: 0; bottom: 0;
    display: flex;
    flex-direction: column;
    align-items: center;
    justify-content: center;
    font-family: 'Arimo', sans-serif;
    font-size: 15px;
    line-height: 1.35;
    color: var(--ink);
    font-style: normal;
  }
  /* Back: brand side */
  .card--back {
    background: var(--navy-deep);
    display: flex;
    align-items: center;
    justify-content: center;
  }
  .card--back .wordmark {
    font-family: 'Cinzel', serif;
    font-weight: 500;
    font-size: 36px;
    color: #3a78c6;
    letter-spacing: 1px;
  }
</style>
</head>
<body>
  <section class="card card--front" aria-label="Business card, contact side">
    <div class="brand">Quillfen Holdings</div>
    <div class="band">
      <div class="person">
        <div class="person__name">Edmund Thorne</div>
        <div class="person__title">Managing Director</div>
      </div>
      <span class="band__divider"></span>
      <ul class="contact">
        <li>044-987 210 365</li>
        <li>hello@quillfen.com</li>
        <li>www.quillfenholdings.com</li>
      </ul>
    </div>
    <address class="address">
      <span>Level 14, Harbour Crest, 52 Wattle Lane,</span>
      <span>Sydney New South Wales 2000, Australia</span>
    </address>
  </section>

  <section class="card card--back" aria-label="Business card, brand side">
    <div class="wordmark">Quillfen Holdings</div>
  </section>
</body>
</html>
```